*** Business Card Design Project

I need a logo and business card for my new catering business: "Pomelia". The design should be modern, clean, elegant and refined. One or Two colours only. The design SHOULD NOT include graphics or images. There should be space for my name, phone number and email address (I will provide these to you later).

Industry/Entity Type

Catering

Requirements
Must have
• Must have one or two colours only.
Must include the text "pomelia"
Should not have
• Must not have graphics or images.

```html
<!DOCTYPE html>
<html lang="en">
<head>
<meta charset="utf-8">
<title>Pomelia Catering – Business Cards</title>
<link rel="stylesheet" href="https://fonts.googleapis.com/css2?family=Tinos&display=swap">
<style>
  :root {
    --sheet: #ffffff;
    --sheet-edge: #6d6d6d;
    --card-yellow: #fdf47e;
    --glow: #ffffff;
    --ink: #1d1a14;
    --leaf: #7dbf2e;
  }
  * { margin: 0; padding: 0; box-sizing: border-box; }
  html, body {
    width: 985px;
    height: 1200px;
    overflow: hidden;
    background: var(--sheet);
  }
  .sheet {
    position: relative;
    width: 985px;
    height: 1200px;
    border: 2px solid var(--sheet-edge);
    background: var(--sheet);
    font-family: "Tinos", "Times New Roman", serif;
    color: var(--ink);
  }
  .card {
    position: absolute;
    width: 811px;
    height: 507px;
    background: var(--card-yellow);
    overflow: hidden;
  }
  .card--front { left: 101px; top: 71px; }
  .card--back  { left: 111px; top: 612px; }

  .card__glow {
    position: absolute;
    border-radius: 50%;
    background: radial-gradient(circle, var(--glow) 0%, rgba(255,255,255,0.75) 30%, rgba(255,255,255,0) 70%);
  }
  .card--front .card__glow { left: 133px; top: -17px; width: 460px; height: 460px; }
  .card--back  .card__glow { left: -17px; top: -82px; width: 380px; height: 380px; }

  .wordmark {
    position: absolute;
    display: flex;
    flex-direction: column;
    align-items: flex-end;
  }
  .wordmark__row {
    display: flex;
    align-items: center;
  }
  .wordmark__dot {
    border-radius: 50%;
    background: var(--leaf);
  }
  .wordmark__name {
    font-weight: 400;
    line-height: 1;
    color: var(--ink);
  }
  .wordmark__tagline {
    line-height: 1;
    color: var(--ink);
  }

  .card--front .wordmark { left: 240px; top: 150px; }
  .card--front .wordmark__dot { width: 62px; height: 62px; margin-right: 14px; }
  .card--front .wordmark__name { font-size: 92px; }
  .card--front .wordmark__tagline { font-size: 28px; margin-top: -4px; }

  .card--back .wordmark { left: 59px; top: 52px; }
  .card--back .wordmark__dot { width: 54px; height: 54px; margin-right: 12px; }
  .card--back .wordmark__name { font-size: 80px; }
  .card--back .wordmark__tagline { font-size: 25px; margin-top: -4px; }

  .card__email {
    position: absolute;
    right: 5px;
    bottom: 14px;
    font-size: 27px;
    letter-spacing: 0.5px;
    color: var(--ink);
  }
</style>
</head>
<body>
  <main class="sheet">
    <section class="card card--front" aria-label="Business card front">
      <div class="card__glow"></div>
      <div class="wordmark">
        <div class="wordmark__row">
          <span class="wordmark__dot"></span>
          <span class="wordmark__name">Pomelia</span>
        </div>
        <span class="wordmark__tagline">catering</span>
      </div>
    </section>

    <section class="card card--back" aria-label="Business card back">
      <div class="card__glow"></div>
      <div class="wordmark">
        <div class="wordmark__row">
          <span class="wordmark__dot"></span>
          <span class="wordmark__name">Pomelia</span>
        </div>
        <span class="wordmark__tagline">catering</span>
      </div>
      <p class="card__email">pomelia@..mail.com</p>
    </section>
  </main>
</body>
</html>
```